Figlantern.com, vietnam local business need a webpage design

We need a web page design for a new business called Figlantern based in Ho Chi Min City, Vietnam. Figlantern sells high quality organic chestnut freshly roasted daily to provide a delicious healthy snack. Figlantern also has a sub-brand called ricepuddleway that sells soya bean curd. Figlantern domain name has been registered as figlantern.com and current Facebook page at Facebook.com/thefiglantern contains photos and other information.
We will like to see web page designs that is visually appealing and representative of our biz. The final design should communicates our core values and growth focus.
Updates

added ricepuddlway signage and Fb QR code

Target Market(s)

Consumer market, household, age range 18-50

Industry/Entity Type

Business

Requirements
Must have
• HTML5
Contain the following sections
- about us & contact us
- Outlets/Locations and locate-us (via google maps)
- Call to order
- Products
- Freshly Roasted Chestnuts
- Raw Chestnuts
- Soya Bean Curd
- Franchise Info
- Photo Gallery
Multi-language support - Vietnamese, English, Korean, Mandarin and Japanese
Mobile device support
- redirect based on browser header
- mobile device friendly format
- IPhone, iPad, Galaxy, Note
- locate/direct me to store (via google maps)
Should not have
• Flash, music, no pop-up

```html
<!DOCTYPE html>
<html lang="en">
<head>
<meta charset="utf-8">
<title>About Us – Figlantern</title>
<link rel="stylesheet" href="https://fonts.googleapis.com/css2?family=Arimo:wght@400;700&family=Roboto+Condensed:wght@400;700&display=swap">
<style>
:root{
  --maroon:#4b0101;
  --red:#e2221f;
  --red-dark:#c7140f;
  --yellow:#fff200;
  --orange:#f08a12;
  --text:#555;
  --heading:#3a0b05;
  --grey-box:#f3f3f3;
  --footer:#e4e4e4;
  --footer-bar:#c9c9c9;
  --white:#fff;
}
*{margin:0;padding:0;box-sizing:border-box}
html,body{width:839px;height:1200px;overflow:hidden;background:var(--white)}
body{position:relative;font-family:Arimo,Arial,sans-serif;color:var(--text)}
a{color:inherit;text-decoration:none}
ul{list-style:none}

.topbar{position:absolute;top:0;left:0;width:839px;height:52px}
.social{position:absolute;left:18px;top:16px;display:flex;gap:4px}
.social span{width:20px;height:20px;background:#bdbdbd}
.social span:first-child{background:#3b5998}
.social span:nth-child(2){background:#c4c4c4}
.lang{position:absolute;right:17px;top:11px;width:130px;height:24px;background:#222;border:1px solid #555;display:flex;align-items:center;font-size:11px;color:#ddd}
.lang .flag{width:15px;height:12px;background:#da251d;margin:0 9px 0 5px}
.lang .arrow{margin-left:auto;width:24px;height:22px;border-left:1px solid #555;display:flex;align-items:center;justify-content:center}

.brandbar{position:absolute;top:52px;left:0;width:839px;height:55px;background:var(--maroon);color:var(--white);font-size:14px}
.brandbar .mail{position:absolute;left:18px;top:19px;display:flex;align-items:center;gap:7px}
.brandbar .phone{position:absolute;right:18px;top:19px;display:flex;align-items:center;gap:6px}
.logo-tab{position:absolute;left:248px;top:0;width:347px;height:52px;background:var(--white)}
.logo{position:absolute;left:340px;top:50px;width:160px;height:46px;display:flex;align-items:center;justify-content:center;gap:8px;font-family:"Roboto Condensed",sans-serif;font-weight:700;font-size:24px;color:var(--white)}
.logo i{width:14px;height:14px;border-radius:50%;background:var(--orange)}

.mainnav{position:absolute;top:107px;left:0;width:839px;height:41px;background:linear-gradient(var(--red),var(--red-dark))}
.mainnav ul{position:absolute;left:134px;top:0;display:flex;height:41px}
.mainnav a{display:block;height:41px;line-height:41px;padding:0 13px;font-family:"Roboto Condensed",sans-serif;font-size:16.5px;color:var(--white)}
.mainnav a.current{background:var(--yellow);color:var(--red)}

.pagehead{position:absolute;top:148px;left:0;width:839px;height:112px;background:linear-gradient(90deg,#d9b8ad,#cfa79a 40%,#e0c6bc 70%,#d6b0a4)}
.pagehead h1{position:absolute;left:26px;top:40px;font-family:"Roboto Condensed",sans-serif;font-size:28px;font-weight:700;color:var(--heading)}
.crumbs{position:absolute;left:26px;top:91px;font-size:11px;color:#222}
.crumbs span{color:var(--red)}

.about{position:absolute;top:282px;left:18px;width:805px}
.about h2{font-family:"Roboto Condensed",sans-serif;font-size:17px;font-weight:400;color:var(--orange);padding-bottom:12px;border-bottom:1px solid #ddd;position:relative}
.about h2::after{content:"";position:absolute;left:0;bottom:-1px;width:119px;height:2px;background:var(--orange)}
.about .body{margin-top:11px;font-size:11.6px;line-height:18px;letter-spacing:-0.15px;text-align:justify;hyphens:auto;-webkit-hyphens:auto}
.about .body p{margin-bottom:7px}
.about .body p.after-photo{clear:both;padding-top:4px}
.team-photo{float:left;width:403px;height:261px;margin:0 14px 10px 0;border:4px solid #c9c9c9;background:linear-gradient(135deg,#8a6a4d,#4a2f22 55%,#b48a64)}

.contact{position:absolute;top:808px;left:18px;width:805px;height:147px;background:var(--grey-box);box-shadow:0 8px 6px -6px rgba(0,0,0,.45)}
.contact .col{position:absolute;top:15px}
.contact h3{display:flex;align-items:center;gap:6px;font-family:"Roboto Condensed",sans-serif;font-size:16px;font-weight:400;color:#555;margin-bottom:14px}
.contact address{font-style:normal;font-size:12px;line-height:22px}
.contact address strong{font-size:13px;color:#555}
.contact .lines p{font-size:13px;margin-bottom:13px}
.contact .lines a{color:var(--orange)}
.map{width:250px;height:74px;border:2px solid #ccc;background:linear-gradient(135deg,#e8e4dc,#d6dccc 60%,#cfe0ea)}

.site-footer{position:absolute;top:983px;left:0;width:839px;height:185px;background:var(--footer)}
.site-footer .col{position:absolute;top:20px}
.site-footer h4{font-family:"Roboto Condensed",sans-serif;font-size:17px;font-weight:400;color:#111;margin-bottom:8px}
.site-footer li,.site-footer p{font-size:11px;line-height:17px;color:#555}
.site-footer li.current{color:var(--red)}
.gallery{display:grid;grid-template-columns:repeat(3,48px);gap:10px 10px}
.gallery span{height:48px;border:2px solid var(--white);background:linear-gradient(#b98a6e,#5a3b2c)}
.copyright{position:absolute;top:1168px;left:0;width:839px;height:32px;background:var(--footer-bar);text-align:center;line-height:32px;font-size:11px;color:#555}
</style>
</head>
<body>

<header>
  <div class="topbar">
    <div class="social" aria-label="Social links"><span></span><span></span><span></span><span></span><span></span><span></span><span></span></div>
    <div class="logo-tab"></div>
    <div class="lang"><span class="flag"></span>Vietnamese<span class="arrow"><svg width="9" height="6"><path d="M0 0h9L4.5 6z" fill="#fff"/></svg></span></div>
  </div>
  <div class="brandbar">
    <a class="mail" href="mailto:info@figlantern.com"><svg width="17" height="13" viewBox="0 0 17 13"><path d="M1 2h15v10H1z" fill="none" stroke="#fff" stroke-width="1.6"/><path d="M1 2l7.5 6L16 2" fill="none" stroke="#fff" stroke-width="1.6"/></svg>info@figlantern.com</a>
    <div class="phone"><svg width="16" height="16" viewBox="0 0 16 16"><path d="M3 1l3 3-2 2c1 2 3 4 5 5l2-2 3 3-2 3C7 15 1 9 1 3z" fill="#fff"/></svg>123- 456-7890</div>
  </div>
  <div class="logo"><i></i>Figlantern</div>
  <nav class="mainnav">
    <ul>
      <li><a class="current" href="#">Home</a></li>
      <li><a href="#">About Us</a></li>
      <li><a href="#">Service</a></li>
      <li><a href="#">Where to Buy</a></li>
      <li><a href="#">Recipes</a></li>
      <li><a href="#">Products</a></li>
      <li><a href="#">Contact</a></li>
    </ul>
  </nav>
</header>

<section class="pagehead" role="img" aria-label="Banner photo of roasted chestnuts">
  <h1>About US</h1>
  <div class="crumbs">Home &nbsp;»&nbsp; <span>About Us</span></div>
</section>

<main class="about">
  <h2>Lorem ipsum dolor sit amet consectetur adipiscing elit.</h2>
  <div class="body">
    <div class="team-photo" role="img" aria-label="Photo of the team standing beside the roasting cart"></div>
    <p>Lorem ipsum dolor sit amet, consectetur adipiscing elit. Morbi congue consequat mauris eget malesuada.</p>
    <p>Vestibulum sit amet lacinia ante. Nullam mattis sit amet est at scelerisque. Nunc eu purus dui. Etiam blandit enim risus, id vulputate dui pellentesque a. Sed bibendum risus vel commodo feugiat. Vestibulum tincidunt lectus ante. Etiam accumsan turpis eu ante accumsan dictum. Cum sociis natoque penatibus et magnis dis parturient montes, nascetur ridiculus mus. Nunc malesuada dignissim convallis. Aenean pellentesque mollis nisi, sed scelerisque nisi tempus vel. Vivamus mi nulla, dapibus a commodo sit amet, feugiat in quam. Aenean vitae urna id est semper luctus.</p>
    <p>Nunc porta feugiat ipsum, vitae bibendum mi. Sed fermentum urna at urna rutrum, ut molestie augue pretium. Donec ac suscipit nisi. Donec vestibulum orci eget leo fermentum, in lobortis elit luctus. Aliquam eros lectus, iaculis non fringilla ac, eleifend id sem. Sed ligula felis, fermentum eu neque et,</p>
    <p class="after-photo">Lorem ipsum dolor sit amet, consectetur adipiscing elit. Morbi congue consequat mauris eget malesuada. Vestibulum sit amet lacinia ante. Nullam mattis sit amet est at scelerisque. Nunc eu purus dui. Etiam blandit enim risus, id vulputate dui pellentesque a. Sed bibendum risus vel commodo feugiat. Vestibulum tincidunt lectus ante. Etiam accumsan turpis eu ante accumsan dictum. Cum sociis natoque penatibus et magnis dis parturient montes, nascetur ridiculus mus. Nunc malesuada dignissim convallis. Aenean pellentesque mollis nisi, sed scelerisque nisi tempus vel. Vivamus mi nulla, dapibus a commodo sit amet, feugiat in quam. Aenean vitae urna id est semper luctus.</p>
    <p>Nunc porta feugiat ipsum, vitae bibendum mi. Sed fermentum urna at urna rutrum, ut molestie augue pretium. Donec ac suscipit nisi. Donec vestibulum orci eget leo fermentum, in lobortis elit luctus. Aliquam eros lectus, iaculis non fringilla ac, eleifend id sem. Sed ligula felis, fermentum eu neque et, accumsan venenatis est. Donec dignissim sed libero et ullamcorper. Vestibulum non fringilla nunc. Donec aliquam tempor justo. Suspendisse eget justo quis nunc vulputate scelerisque. Morbi felis tortor, accumsan id sollicitudin ut, rutrum et magna. Fusce sed odio dictum, aliquam lorem consequat, pellentesque sapien.</p>
  </div>
</main>

<section class="contact">
  <div class="col" style="left:20px">
    <h3><svg width="17" height="15" viewBox="0 0 17 15"><path d="M8.5 0L17 7h-2.5v8h-4v-5h-4v5h-4V7H0z" fill="#666"/></svg>Location</h3>
    <address><strong>Figlantern</strong><br>2013 4th Street,<br>Figlantern&nbsp; Street<br>Ho Chi Min City, Vietnam.</address>
  </div>
  <div class="col lines" style="left:255px">
    <h3><svg width="11" height="17" viewBox="0 0 11 17"><rect x="1" y="1" width="9" height="15" rx="1.5" fill="none" stroke="#666" stroke-width="1.8"/><rect x="4" y="13" width="3" height="1.5" fill="#666"/></svg>Phone</h3>
    <p>Tel: 123.456.7890</p>
    <p>Fax: 123.456.7890</p>
    <p>Email: <a href="mailto:info@figlantern.com">info@figlantern.com</a></p>
  </div>
  <div class="col" style="left:534px">
    <h3><svg width="13" height="17" viewBox="0 0 13 17"><path d="M6.5 0A6 6 0 0 1 12.5 6c0 4-6 11-6 11S.5 10 .5 6a6 6 0 0 1 6-6z" fill="#666"/><circle cx="6.5" cy="6" r="2.3" fill="#f3f3f3"/></svg>Location on&nbsp; map</h3>
    <div class="map" role="img" aria-label="Street map of Ho Chi Min City with the store marked"></div>
  </div>
</section>

<footer class="site-footer">
  <div class="col" style="left:18px">
    <h4>Menu</h4>
    <ul><li class="current">Home</li><li>About Us</li><li>Service</li><li>Where to Buy</li><li>Recipes</li><li>Products</li><li>Contact</li></ul>
  </div>
  <div class="col" style="left:132px;width:160px">
    <h4>Service</h4>
    <p>Duis et nibh libero. Praesent bibedum mi risus, ac rhoncus leo cursus&nbsp; Maecenas tellus ipsum, auctor id consequat ac, tempus uis dolor. Phasellus condimentum,e eu vulputate ultricies, urna neque bibendum</p>
  </div>
  <div class="col" style="left:333px;width:160px">
    <h4>Service</h4>
    <p>Duis et nibh libero. Praesent bibedum mi risus, ac rhoncus leo cursus&nbsp; Maecenas tellus ipsum, auctor id consequat ac, tempus uis dolor. Phasellus condimentum,e eu vulputate ultricies, urna neque bibendum</p>
  </div>
  <div class="col" style="left:532px">
    <h4>Products</h4>
    <ul><li>Duisetnibh libero</li><li>Praesentbibedum</li><li>Mirisusacrncus</li><li>Leocursuscenas</li><li>Tllusduisetnibh</li><li>libero.praesent</li><li>Mirisusacrncus</li></ul>
  </div>
  <div class="col" style="left:659px">
    <h4>Photo&nbsp; Gallery</h4>
    <div class="gallery">
      <span role="img" aria-label="Gallery photo 1"></span>
      <span role="img" aria-label="Gallery photo 2"></span>
      <span role="img" aria-label="Gallery photo 3"></span>
      <span role="img" aria-label="Gallery photo 4"></span>
      <span role="img" aria-label="Gallery photo 5"></span>
      <span role="img" aria-label="Gallery photo 6"></span>
    </div>
  </div>
</footer>
<div class="copyright">© 2013 Copyright. figlantern</div>

</body>
</html>
```